依頼詳細
2024年の年賀状のデザインをお願いします(裏面のみ)。

明るく元気で遊び心のあるデザインを希望します。
添付の当社ロゴを一部(どれでもOK)をお使い下さい。
ポイント的に使っていただいても、ロゴ自体を強調していただいてもどちらでも構いません。
干支的要素を入れていただいてもなくてもどちらでも構いません。

HP: http://www.moru-works.co.jp/

※昨年度までもツクバーの方にデザインしていただいています。
ご応募いただいた作品はこちらです。

2014年
http://www.tsukuba-hub.jp/work/detail/510327

2015年
http://www.tsukuba-hub.jp/work/detail/630418

2016年
http://www.tsukuba-hub.jp/work/detail/920461

2017年
http://www.tsukuba-hub.jp/work/detail/1490356

2018年
https://www.tsukuba-hub.jp/work/detail/1860542

2019年
https://www.tsukuba-hub.jp/work/detail/2470193

2020年
https://www.tsukuba-hub.jp/work/detail/2950684

2021年
https://www.tsukuba-hub.jp/work/detail/3580427

2022年
https://www.tsukuba-hub.jp/work/detail/3920175

2023年
https://www.tsukuba-hub.jp/work/detail/4610238
記載項目
1.MRWのロゴ

※MRWの文字は添付ロゴデータから切り貼りしてお使い下さい。
※MRWの文字はデザインの一部として織り込んで下さい。

2.テキスト

明けましておめでとうございます。
本年も変わらぬお引き立てのほど宜しくお願い申し上げます。

〒104-0038 東京都中央区新富町2-318 新富町桜葉ビルディング
TEL:03-5914-2730

※すっきりと見やすいテキストレイアウトをお願いします。
希望イメージ
シンプル 複雑
単色 カラフル
暗い 明るい
日常 高級
遊び心 厳粛
未来的 伝統的
女性的 男性的
納品ファイル
• 高解像度JPG (.jpg)
• イラストレーター形式 (.ai)
補足説明
添付のロゴデータを一部、織り込んで下さい。
■ 選んだ理由

力作揃いで今年も社内で票が割れました。ほぼ横並びの中で、社長の推しを当選作として選ばせていただきました。
(次点には、最後まで競り合った候補作を選ばせていただきました)

■ 提案者全員のお礼・コメント

今年もたくさんご応募をありがとうございました。
ここ数年で一番多いご応募をいただき、嬉しい悲鳴の中、役員と選定を進めさせていただきました。
ストレートなデザインからヒネったもの、題材も竜や龍からタツノオトシゴまで、みなさまの創意工夫には驚かされることが多いです。

こんなご時世で、この先どうなるかは分かりませんが、来年もできればお願いすると思いますので、ご提案いただければ幸いです。
みなさま、良いお年をお迎えください。

```html
<!DOCTYPE html>
<html lang="ja">
<head>
<meta charset="utf-8">
<title>2024 年賀状 MRW</title>
<link rel="stylesheet" href="https://fonts.googleapis.com/css2?family=Klee+One:wght@600&family=Noto+Sans+JP:wght@500;700;900&display=swap">
<style>
  :root {
    --card-yellow: #f6d22c;
    --moon-white: #ffffff;
    --ink: #1b1b1b;
    --wave-white: #ffffff;
  }
  html, body {
    margin: 0;
    padding: 0;
    overflow: hidden;
    background: var(--card-yellow);
  }
  .card {
    position: relative;
    width: 810px;
    height: 1200px;
    background: var(--card-yellow);
    overflow: hidden;
    font-family: "Noto Sans JP", sans-serif;
    color: var(--ink);
  }
  .scene {
    position: absolute;
    inset: 0;
  }
  .year {
    position: absolute;
    top: 148px;
    left: 0;
    width: 100%;
    margin: 0;
    text-align: center;
    font-family: "Klee One", cursive;
    font-weight: 600;
    font-size: 58px;
    line-height: 1;
    letter-spacing: 4px;
  }
  .greeting {
    position: absolute;
    top: 214px;
    left: 0;
    width: 100%;
    margin: 0;
    text-align: center;
    font-weight: 900;
    font-size: 40px;
    line-height: 52px;
    letter-spacing: 2px;
  }
  .company-name {
    position: absolute;
    top: 374px;
    left: 0;
    width: 100%;
    margin: 0;
    text-align: center;
    font-weight: 700;
    font-size: 60px;
    line-height: 1;
    letter-spacing: 16px;
    text-indent: 16px;
  }
  .message {
    position: absolute;
    top: 866px;
    left: 0;
    width: 100%;
    margin: 0;
    text-align: center;
    font-weight: 700;
    font-size: 30px;
    line-height: 46px;
  }
  .contact {
    position: absolute;
    top: 1004px;
    left: 200px;
    margin: 0;
    text-align: left;
    font-weight: 700;
    font-size: 22px;
    line-height: 38px;
    font-style: normal;
    white-space: nowrap;
  }
  .contact .gap { display: inline-block; width: 16px; }
</style>
</head>
<body>
<main class="card">
  <svg class="scene" width="810" height="1200" viewBox="0 0 810 1200">
    <circle class="moon" cx="405" cy="285" r="296" fill="var(--moon-white)"/>
    <rect class="dragon-silhouette" role="img" aria-label="水面から立ち上がる龍のシルエットのイラスト" x="325" y="470" width="300" height="92" rx="30" fill="var(--ink)"/>
    <rect x="0" y="562" width="810" height="120" fill="var(--card-yellow)"/>
    <g class="water-lines" stroke="var(--wave-white)" stroke-linecap="round">
      <line x1="105" y1="562" x2="715" y2="562" stroke-width="5"/>
      <line x1="245" y1="588" x2="580" y2="588" stroke-width="4"/>
      <line x1="290" y1="610" x2="540" y2="610" stroke-width="4"/>
      <line x1="330" y1="630" x2="500" y2="630" stroke-width="3"/>
    </g>
  </svg>

  <p class="year">2024</p>
  <h1 class="greeting">明けましておめでとう<br>ございます。</h1>
  <p class="company-name">MRW</p>

  <p class="message">本年も変わらぬお引き立ての<br>ほど宜しくお願い申し上げます。</p>

  <address class="contact">
    〒104-0038<span class="gap"></span>東京都中央区新富町2-318<br>
    新富町桜葉ビルディング<br>
    TEL 03-5914-2730<span class="gap"></span>HP http://www.moru-works.co.jp/
  </address>
</main>
</body>
</html>
```